Website template and forms
Velvet lantern
Website template and forms  - Financial Services
Creative Brief
Financial Services
http://www.velvet-lantern.co.uk
Velvet Lantern works as an intermediary between clients who are looking into products such as life insurance and the IFA and Brokerage community who can assist them.
We have teamed up with some of the countries largest survey companies and respond directly to customers who have suggested they may be interested in learning more.
General knowledge about life insurance and how it operates is limited within what the industry terms “the insurance gap” and our aim is to ensure our customers understand the products they are interested in and they feel the products are suitable for them.
Whilst we do not provide or offer advice at any time, we spend time talking with customers about their need for cover. We find a lot of our customers have made the decision that they need to have cover in place but have yet to think about how much cover they require and over what time period. This can cause difficulties when calling into brokerages directly or indeed when using comparison sites, where you are asked direct questions and are not always equipped with the answers. This can then be a frustrating process for all involved.
We have essentially two sets of customers, the customers who respond to surveys and whom we then call and assist and also the IFA/Brokerages with whom we place our leads.
We will only transfer a client to a brokerage when they have a good understanding of what they are looking for, often we can outline the areas to think about and arrange to call the client back. This works for everyone concerned as the buyer knows what they are looking for and understands what the product does and doesn’t do and also ensures that the commercial side of our business, which is lead provision maintains its reputation.
We have long term relationships with our clients and companies have chosen us as their sole partner for Life insurance transfers. We work continually on our approach and service so that brokerages receive those customers whom they feel they can benefit; taking daily feedback on every lead we supply to ensure standards are high.
Each brokerage has its own set of criteria and parameters for customers, for example IFA companies who like to advise clients need the customers to have enough time to spare to complete a fact find and have their needs assessed. Brokerages offer a quick and comprehensive service often finding customers much more competitive products than they would otherwise have access to.
Like : Exisiting logo. Dislikes: Flash, moving images, unindexable content
Colorful
Humorous
yellow
what ever works
Arial, Verdana, Trebuchet MS, Times New Roman, Century Gothic, Georgia
left side
please email derek@velvet-lantern.co.uk for the full design brief. We also need some auto email forms creating as part of the project. Please inform me if you cannot do this.

```html
<!DOCTYPE html>
<html lang="en">
<head>
<meta charset="utf-8">
<title>Velvet Lantern – Financial Services</title>
<link href="https://fonts.googleapis.com/css2?family=Questrial&family=Arimo:wght@400;700&display=swap" rel="stylesheet">
<style>
:root{
  --purple-dark:#4d4f9a;
  --purple:#6e71bd;
  --purple-light:#a6a8e0;
  --page:#eceef6;
  --white:#ffffff;
  --orange:#f2a81c;
  --orange-deep:#e08a00;
  --gold:#f0b400;
  --heading-orange:#f0a020;
  --heading-purple:#5a5db0;
  --box-dark:#3a3a3a;
  --box-mid:#5c5c5c;
  --text-light:#f2f2f2;
}
*{box-sizing:border-box;margin:0;padding:0}
html,body{width:1200px;height:746px;overflow:hidden}
body{
  position:relative;
  background:linear-gradient(90deg,#d7d8ec 0,var(--page) 13%,var(--page) 87%,#d7d8ec 100%);
  font-family:"Arimo",Arial,sans-serif;
}
.site-nav{
  position:absolute;left:0;top:0;width:1200px;height:50px;
  background:linear-gradient(180deg,var(--purple-light) 0,var(--purple) 55%,var(--purple-dark) 100%);
  font-family:"Questrial","Century Gothic",sans-serif;
}
.nav-item{position:absolute;top:14px;color:var(--white);font-size:19px;text-decoration:none}
.nav-item.is-active{
  top:10px;left:172px;padding:3px 16px;border-radius:14px;
  background:var(--white);color:var(--orange-deep);font-size:17px;
}
.search-field{
  position:absolute;left:776px;top:14px;width:184px;height:24px;
  border:1px solid #ccc;background:var(--white);font-size:12px;padding:4px 6px;color:#333;
}
.search-button{
  position:absolute;left:968px;top:14px;width:70px;height:24px;border-radius:3px;
  background:linear-gradient(#fafafa,#d8d8d8);border:1px solid #aaa;
  font:700 13px "Arimo",Arial,sans-serif;color:#222;text-align:center;line-height:22px;
}
.hero{
  position:absolute;left:156px;top:76px;width:888px;height:322px;
  border:3px solid var(--gold);
  background:var(--white);
  overflow:hidden;
}
.hero-photo{
  position:absolute;inset:0;
  background:linear-gradient(100deg,#ffffff 0,#f3f6fb 35%,#dfe6f1 60%,#cfd8e8 100%);
}
.hero-character{
  position:absolute;left:14px;top:8px;width:150px;height:296px;border-radius:60px 60px 20px 20px;
  background:radial-gradient(ellipse at 50% 40%,#6a9be0 0,#3f70c8 55%,rgba(63,112,200,0) 72%);
}
.brand-name{
  position:absolute;left:172px;top:112px;
  font-family:"Questrial","Century Gothic",sans-serif;font-size:44px;line-height:1.05;
  color:var(--orange-deep);
}
.service-links{position:absolute;left:632px;top:46px;width:200px}
.service-link{
  position:absolute;left:0;width:196px;height:34px;border-radius:3px;
  background:linear-gradient(180deg,#ffc440 0,var(--orange) 55%,var(--orange-deep) 100%);
  color:var(--white);font-size:16px;line-height:34px;padding-left:44px;
  box-shadow:0 2px 3px rgba(0,0,0,.25);
}
.service-link svg{position:absolute;left:6px;top:5px}
.service-link.is-tall{height:42px;line-height:1.1;padding-top:4px}
.service-link.is-tall span{font-size:12px;display:block}
.section-title{
  position:absolute;top:424px;font-family:"Questrial","Century Gothic",sans-serif;
  font-style:italic;font-weight:400;font-size:30px;line-height:38px;
}
.section-title.is-reasons{left:176px;color:var(--heading-orange)}
.section-title.is-quote{left:780px;color:var(--heading-purple)}
.reason{
  position:absolute;width:274px;height:90px;border-radius:10px;
  background:linear-gradient(180deg,var(--box-mid) 0,var(--box-dark) 100%);
  box-shadow:0 2px 4px rgba(0,0,0,.35);
}
.reason-icon{
  position:absolute;left:8px;top:10px;width:66px;height:68px;border-radius:8px;
  background:linear-gradient(160deg,#ffffff 0,#dfe8f5 100%);
}
.reason-text{
  position:absolute;left:82px;top:8px;width:160px;color:var(--text-light);
  font-size:9.5px;line-height:1.22;
}
.reason-more{position:absolute;right:40px;bottom:5px;color:var(--white);font-size:9px;font-weight:700}
.reason-arrow{position:absolute;right:-4px;top:31px}
.site-footer{
  position:absolute;left:154px;top:708px;width:892px;height:30px;
  background:linear-gradient(180deg,var(--purple-light) 0,var(--purple) 50%,var(--purple-dark) 100%);
  color:var(--white);font-size:11px;font-weight:700;
}
.footer-copy{position:absolute;left:10px;top:9px}
.newsletter{position:absolute;left:506px;top:9px}
.newsletter-field{
  position:absolute;left:706px;top:5px;width:114px;height:19px;background:var(--white);
  border:1px solid #bbb;color:#333;font-size:10px;font-weight:400;padding:3px 4px;
}
.newsletter-button{
  position:absolute;left:826px;top:5px;width:58px;height:19px;border-radius:2px;
  background:linear-gradient(#fafafa,#d6d6d6);border:1px solid #999;
  color:#222;font-size:10px;text-align:center;line-height:17px;
}
</style>
</head>
<body>
<nav class="site-nav">
  <a class="nav-item is-active" href="#">Home</a>
  <a class="nav-item" style="left:302px" href="#">About Us</a>
  <a class="nav-item" style="left:442px" href="#">Leave a Comment</a>
  <a class="nav-item" style="left:644px" href="#">Contact Us</a>
  <div class="search-field">Find It</div>
  <div class="search-button">Search</div>
</nav>

<section class="hero">
  <div class="hero-photo" role="img" aria-label="Soft photo of an insurance application form with a pen"></div>
  <div class="hero-character" role="img" aria-label="Cartoon lantern spirit mascot holding a coin bag above a golden lamp"></div>
  <div class="brand-name">Velvet<br>Lantern</div>
  <div class="service-links">
    <div class="service-link" style="top:0">
      <svg width="30" height="24" viewBox="0 0 30 24"><path d="M2 8h16V2l10 10-10 10v-6H2z" fill="#b56a00" opacity=".55"/></svg>Life Insurance
    </div>
    <div class="service-link" style="top:54px">
      <svg width="30" height="24" viewBox="0 0 30 24"><path d="M2 8h16V2l10 10-10 10v-6H2z" fill="#b56a00" opacity=".55"/></svg>Broker Area
    </div>
    <div class="service-link" style="top:110px">
      <svg width="30" height="24" viewBox="0 0 30 24"><path d="M2 8h16V2l10 10-10 10v-6H2z" fill="#b56a00" opacity=".55"/></svg>Home Insurance
    </div>
    <div class="service-link is-tall" style="top:168px">
      <svg width="30" height="24" viewBox="0 0 30 24"><path d="M2 8h16V2l10 10-10 10v-6H2z" fill="#b56a00" opacity=".55"/></svg><span>Over 50 Life Insurance</span>No Medicals
    </div>
  </div>
</section>

<h2 class="section-title is-reasons">Reasons to choose us</h2>
<h2 class="section-title is-quote">Get a Quote Now</h2>

<article class="reason" style="left:172px;top:480px">
  <div class="reason-icon" role="img" aria-label="Icon of a computer screen"></div>
  <p class="reason-text">Velvet Lantern works as an intermediary between clients who are looking into products such as life insurance and the IFA and Brokerage...</p>
  <span class="reason-more">Read More</span>
  <svg class="reason-arrow" width="26" height="26" viewBox="0 0 26 26"><circle cx="13" cy="13" r="12" fill="#2a2a2a" stroke="#777"/><path d="M10 7l7 6-7 6z" fill="#fff"/></svg>
</article>
<article class="reason" style="left:468px;top:480px">
  <div class="reason-icon" role="img" aria-label="Icon of an umbrella sheltering a family"></div>
  <p class="reason-text">We have teamed up with some of the countries largest survey companies and respond directly to customers who have suggested...</p>
  <span class="reason-more">Read More</span>
  <svg class="reason-arrow" width="26" height="26" viewBox="0 0 26 26"><circle cx="13" cy="13" r="12" fill="#2a2a2a" stroke="#777"/><path d="M10 7l7 6-7 6z" fill="#fff"/></svg>
</article>
<article class="reason" style="left:764px;top:480px">
  <div class="reason-icon" role="img" aria-label="Icon of hands protecting a house"></div>
  <p class="reason-text">General knowledge about life insurance and how it operates is limited within what the industry terms “the insurance gap” and our aim is to...</p>
  <span class="reason-more">Read More</span>
  <svg class="reason-arrow" width="26" height="26" viewBox="0 0 26 26"><circle cx="13" cy="13" r="12" fill="#2a2a2a" stroke="#777"/><path d="M10 7l7 6-7 6z" fill="#fff"/></svg>
</article>
<article class="reason" style="left:172px;top:594px">
  <div class="reason-icon" role="img" aria-label="Icon of a delivery truck"></div>
  <p class="reason-text">We will only transfer a client to a brokerage when they have a good understanding of what they are looking for, often we can outline the...</p>
  <span class="reason-more">Read More</span>
  <svg class="reason-arrow" width="26" height="26" viewBox="0 0 26 26"><circle cx="13" cy="13" r="12" fill="#2a2a2a" stroke="#777"/><path d="M10 7l7 6-7 6z" fill="#fff"/></svg>
</article>
<article class="reason" style="left:468px;top:594px">
  <div class="reason-icon" role="img" aria-label="Icon of a parcel with circling arrows"></div>
  <p class="reason-text">We have long term relationships with our clients and companies have chosen us as their sole partner for Life insurance transfers...</p>
  <span class="reason-more">Read More</span>
  <svg class="reason-arrow" width="26" height="26" viewBox="0 0 26 26"><circle cx="13" cy="13" r="12" fill="#2a2a2a" stroke="#777"/><path d="M10 7l7 6-7 6z" fill="#fff"/></svg>
</article>
<article class="reason" style="left:764px;top:594px">
  <div class="reason-icon" role="img" aria-label="Icon of coins around a circle"></div>
  <p class="reason-text">Each brokerage has its own set of criteria and parameters for customers, for example IFA companies who like to advise clients need the...</p>
  <span class="reason-more">Read More</span>
  <svg class="reason-arrow" width="26" height="26" viewBox="0 0 26 26"><circle cx="13" cy="13" r="12" fill="#2a2a2a" stroke="#777"/><path d="M10 7l7 6-7 6z" fill="#fff"/></svg>
</article>

<footer class="site-footer">
  <span class="footer-copy">Copyright © 2011 Velvet Lantern | All Rights Reserved</span>
  <span class="newsletter">Subscribe for our Newsletter:</span>
  <div class="newsletter-field">Email:</div>
  <div class="newsletter-button">Subscribe</div>
</footer>
</body>
</html>
```